Small animal veterinary clinic needs a new web site design

We need a new web site design for Harlowe Veterinary Clinic. The clinic performs medicine, surgery, and wellness care for cats and dogs. We have been in business for over 50 years so we want to project stability, reliability, class, elegance, and professionalism. We also want to convey that we have modern facilities and services and perform high quality medicine.
The current web site has been in place for many years and looks stale but for reference it is at http://www.harlowevetcare.example. We will be re-writing most of the content and looking to add additional pages, videos, downloadable documents (forms, brochures, marketing materials, etc.) The new owners prefer a more classy, modern look. Some vet clinic sites we like are http://pintrelpaws.example and http://corvalanimalcare.example. We like a nice, clean, fresh, interactive interface.
Our new logo is attached. We want the color scheme of the web site to be complementary to the colors in the logo, especially the blue and green. The purple color of the text should just be used for accent. Upon request and if necessary, I can supply the Adobe Illustrator source file for the logo.
We are looking for a set of page designs - a great, eye-catching home page and 2-3 content page layouts we can use to create content pages with our own text and other content. Navigation design is very important as well. Again, we can fill in the content of the navigation links but I would like a nice, easy-to-use, logical navigation design. If you want some content or navigation links to use as reference during your design phase, feel free to pull whatever content or navigation you want from our existing web site. I am not looking for just images, I would like actual page files - HTML, CSS, etc.
Thanks and good luck!
Target Market(s)
We cater to pet owners across a wide age range. Socio-economic status of our customers is middle class and above. We do not target price shoppers.
Industry/Entity Type
Veterinary
Colors
Designer to choose colors to be used in the design.
Requirements
Must have
- Must look professional, clean, and modern. We are looking for simple but elegant design and navigation. 1 home page design, 2-3 content page designs delivered with code (HTML & CSS).
Nice to have
- When HTML/CSS is delivered, it would be awesome if it were mobile ready as well.
Should not have
- Colors that are too bold. Layout that is too complex.

```html
<!DOCTYPE html>
<html lang="en">
<head>
<meta charset="utf-8">
<title>Harlowe Veterinary Clinic</title>
<link rel="stylesheet" href="https://fonts.googleapis.com/css2?family=Arimo:wght@400;700&family=Roboto+Condensed:wght@400;700&display=swap">
<style>
:root{
  --purple:#5b1744;
  --purple-dark:#4a1238;
  --teal:#2e9c86;
  --green:#35b07c;
  --blue:#1f5c9c;
  --ink:#3a3a3a;
  --body-text:#4a4a4a;
  --panel-edge:#d6d6d6;
  --white:#ffffff;
}
*{box-sizing:border-box;margin:0;padding:0}
html,body{width:696px;height:1200px;overflow:hidden}
body{position:relative;background:var(--white);font-family:"Arimo",Arial,sans-serif;color:var(--ink)}
.abs{position:absolute}

/* header */
.header-bg{left:0;top:0;width:696px;height:69px;background:linear-gradient(#ffffff,#f1f1f1)}
.brand{left:70px;top:44px;width:84px;text-align:center;font:700 12px/1 "Arimo",Arial,sans-serif;color:var(--purple);letter-spacing:.5px}
.brand-dot{left:104px;top:8px;width:16px;height:16px;border-radius:50%;background:var(--teal)}
.header-photo{left:212px;top:0;width:282px;height:69px;
  background:
    radial-gradient(ellipse 40px 30px at 22% 55%,#c9ab86 0%,rgba(201,171,134,0) 100%),
    radial-gradient(ellipse 34px 38px at 62% 40%,#e6c2a5 0%,rgba(230,194,165,0) 100%),
    radial-gradient(ellipse 30px 26px at 82% 55%,#b58a5e 0%,rgba(181,138,94,0) 100%),
    linear-gradient(90deg,rgba(255,255,255,1) 0%,#efe6dc 25%,#e8d8c6 55%,#f3ebe3 85%,rgba(255,255,255,1) 100%)}
.call{left:556px;top:4px;font-size:8px;color:#666}
.call-icon{left:538px;top:5px}
.phone{left:556px;top:14px;font:700 10px/1 "Arimo",Arial,sans-serif;color:var(--green)}
.follow{left:505px;top:42px;font-size:8px;color:#555}
.social{top:39px;width:15px;height:15px;border-radius:2px}
.s1{left:563px;background:#3b5a9a}.s2{left:584px;background:#3aa7d6}.s3{left:605px;background:#1f6ea3}

/* nav */
.nav{left:0;top:69px;width:696px;height:22px;background:var(--purple)}
.nav a{position:absolute;top:0;height:22px;line-height:22px;font-size:9px;color:#fff;text-decoration:none;text-align:center}
.nav a.active{background:var(--teal);font-weight:700}
.nav .sep{position:absolute;top:5px;width:1px;height:12px;background:rgba(255,255,255,.35)}
.search{left:516px;top:5px;width:102px;height:12px;background:#7a3a65;color:#ddd;font:italic 7px/12px "Arimo",Arial,sans-serif;padding-left:6px}

/* hero */
.hero{left:0;top:91px;width:696px;height:240px;
  background:
    radial-gradient(ellipse 90px 110px at 9% 35%,#f0d2b8 0%,rgba(240,210,184,0) 100%),
    radial-gradient(ellipse 70px 80px at 4% 80%,#e3d8cc 0%,rgba(227,216,204,0) 100%),
    radial-gradient(ellipse 60px 70px at 33% 70%,#d49a5c 0%,rgba(212,154,92,0) 100%),
    radial-gradient(ellipse 110px 80px at 58% 60%,#3a3a3a 0%,rgba(58,58,58,0) 100%),
    radial-gradient(ellipse 80px 70px at 58% 80%,#5a5a5a 0%,rgba(90,90,90,0) 100%),
    radial-gradient(ellipse 70px 90px at 90% 30%,#f2d4bc 0%,rgba(242,212,188,0) 100%),
    radial-gradient(ellipse 90px 70px at 92% 85%,#2a3a66 0%,rgba(42,58,102,0) 100%),
    radial-gradient(ellipse 120px 110px at 78% 20%,#6e8a4a 0%,rgba(110,138,74,0) 100%),
    linear-gradient(90deg,#c79a74 0%,#b58963 22%,#d5c3a8 40%,#9b8f7a 55%,#8a9a6a 75%,#b7a48c 100%)}
.hero-curve{left:0;top:250px}
.dots{left:328px;top:285px}
.dot{display:inline-block;width:7px;height:7px;border-radius:50%;background:var(--teal);margin-right:4px}
.dot.off{background:#c8c8c8}
.tagline{left:0;top:303px;width:696px;text-align:center;font:700 13px/1 "Roboto Condensed",sans-serif;color:var(--purple)}
.tag-big{left:0;top:324px;width:696px;text-align:center;font:700 18px/1 "Roboto Condensed",sans-serif;color:var(--purple)}
.tag-line{top:333px;width:51px;height:2px;background:linear-gradient(90deg,var(--blue),var(--teal))}

/* main panel */
.panel{left:74px;top:436px;width:546px;height:456px;background:linear-gradient(#f4f4f4,#e8e8e8);border:1px solid var(--panel-edge);border-radius:6px;box-shadow:0 2px 4px rgba(0,0,0,.15)}
.services-panel{left:101px;top:888px;width:493px;height:76px;background:#eeeeee;border:1px solid var(--panel-edge);border-top:none;border-radius:0 0 6px 6px;box-shadow:0 2px 4px rgba(0,0,0,.15)}

/* welcome band */
.welcome{left:106px;top:366px;width:476px;height:88px;background:linear-gradient(90deg,#2f2f2f,#454545 50%,#353535)}
.doc-photo{left:112px;top:372px;width:64px;height:72px;border:2px solid #ddd;
  background:radial-gradient(ellipse 14px 16px at 50% 32%,#e2b89a 0%,rgba(226,184,154,0) 100%),
             radial-gradient(ellipse 26px 20px at 50% 90%,#f4f4f4 0%,rgba(244,244,244,0) 100%),
             linear-gradient(#9aa6b0,#6a6f74)}
.bio{left:185px;top:372px;width:144px;font-size:7px;line-height:9.8px;color:#e8e8e8}
.read{font-size:7.5px;color:var(--green);font-weight:700}
.bio-read{left:276px;top:441px}
.badge{left:346px;top:362px;width:68px;height:24px;background:var(--purple);border:2px solid var(--green);transform:rotate(-22deg);color:#fff;font:700 8px/9px "Arimo",Arial,sans-serif;text-align:center;padding-top:2px}
.field{left:414px;width:106px;height:12px;background:#d2d2d2;border:1px solid #aaa;font:italic 6.5px/11px "Arimo",Arial,sans-serif;color:#888;padding-left:4px}
.signup{left:414px;top:438px;width:48px;height:12px;background:var(--teal);color:#fff;font:700 7px/12px "Arimo",Arial,sans-serif;text-align:center}
.dog-art{left:526px;top:378px;width:72px;height:88px;border-radius:40% 40% 12px 12px;
  background:radial-gradient(ellipse 18px 22px at 50% 30%,#3a3330 0%,rgba(58,51,48,0) 100%),
             linear-gradient(#e8e3de,#b9b1a9)}

/* section tabs */
.tab{height:22px;background:#dcdcdc;border-radius:3px;font:700 10px/22px "Roboto Condensed",sans-serif;color:var(--purple);padding-left:10px;box-shadow:0 1px 2px rgba(0,0,0,.15);white-space:nowrap}

/* team */
.rope{left:84px;top:517px;width:524px;height:2px;background:#9b7a5c}
.clip{top:496px;width:6px;height:32px;background:linear-gradient(90deg,#c9a24a,#e6c66e,#b48a32)}
.frame{top:526px;width:76px;height:82px;background:#fff;border:1px solid #ccc;box-shadow:0 1px 3px rgba(0,0,0,.2)}
.frame .pic{position:absolute;left:3px;top:3px;width:68px;height:57px}
.frame p{position:absolute;left:3px;top:63px;width:70px;font-size:6.5px;line-height:7.5px;color:#666}
.arrow{top:558px}

/* about */
.about-text{left:107px;top:657px;width:233px;font-size:7.2px;line-height:10.7px;color:var(--body-text)}
.divider{left:364px;top:640px;width:1px;height:224px;background:#ccc}
.video{left:393px;top:656px;width:188px;height:94px;
  background:radial-gradient(ellipse 60px 20px at 45% 55%,#f3f3f0 0%,rgba(243,243,240,0) 100%),
             linear-gradient(#4f6a48 0%,#8a9a80 25%,#d9d9d4 45%,#c4c4bc 62%,#55624c 80%,#3d4a3a 100%)}
.video-bar{left:393px;top:742px;width:188px;height:8px;background:#1e1e1e}
.play{left:477px;top:687px;width:20px;height:20px;border-radius:50%;background:rgba(255,255,255,.55)}

/* reviews & news */
.nav-circle{top:771px;width:11px;height:11px;border-radius:50%;background:var(--blue)}
.reviewer{left:107px;top:798px;width:45px;height:52px;
  background:radial-gradient(ellipse 10px 12px at 50% 35%,#e2b89a 0%,rgba(226,184,154,0) 100%),
             linear-gradient(#6f8a5a,#3a3a30)}
.quote{left:164px;top:798px;width:177px;font-family:"Arimo",Arial,sans-serif;font-weight:400;font-size:7px;line-height:11.4px;color:var(--body-text);letter-spacing:.3px}
.quote .mark{font-size:11px;font-weight:400;color:#777}
.date{left:394px;width:23px;height:24px;text-align:center}
.date .m{display:block;height:9px;background:var(--green);color:#fff;font:700 6px/9px "Arimo",Arial,sans-serif}
.date .d{display:block;height:15px;background:#d4d4d4;color:#444;font:700 9px/15px "Arimo",Arial,sans-serif}
.news-text{left:425px;width:120px;font-size:7px;line-height:10.5px;color:var(--body-text)}
.cat-art{left:548px;top:804px;width:58px;height:38px;border-radius:50%;background:linear-gradient(135deg,#d7b48a,#9b7652)}

/* services */
.svc-dog{left:186px;top:872px;width:52px;height:88px;border-radius:45% 45% 10px 10px;background:linear-gradient(#9a7a52,#4e3824)}
.svc-cat{left:518px;top:868px;width:50px;height:88px;border-radius:45% 45% 10px 10px;background:linear-gradient(#e8b88a,#f3efe8)}
.svc-list{list-style:none;font-size:7px;line-height:13px;color:#444}
.svc-list li::before{content:"";display:inline-block;width:6px;height:6px;border-radius:50%;background:var(--purple);margin-right:8px;vertical-align:-.5px}

/* footer */
.footer-wave{left:0;top:1030px}
.footer h4{position:absolute;font:700 8px/1 "Arimo",Arial,sans-serif;color:#fff}
.links{list-style:none;font-size:7.5px;line-height:11.2px;color:#fff}
.fdiv{top:1088px;width:1px;height:80px;background:rgba(255,255,255,.25)}
.cta{left:159px;width:105px;height:17px;background:var(--green);color:#fff;font:700 8px/17px "Arimo",Arial,sans-serif;text-align:center}
.foot-brand{left:164px;top:1138px;width:96px;text-align:center;font:700 13px/1 "Arimo",Arial,sans-serif;color:#fff;letter-spacing:.5px}
.hours{font-size:7.5px;line-height:14px;color:#fff}
.map{left:444px;top:1098px;width:76px;height:66px;border:2px solid #ddd;
  background:linear-gradient(160deg,rgba(0,0,0,0) 45%,#f2d27a 46%,#f2d27a 50%,rgba(0,0,0,0) 51%),linear-gradient(135deg,#eceae2,#d6d6cc)}
.addr{font-size:7.5px;line-height:11.8px;color:#fff}
.bottom-bar{left:0;top:1176px;width:696px;height:24px;background:var(--green);color:#fff;font:700 7.5px/24px "Arimo",Arial,sans-serif;text-align:center}
</style>
</head>
<body>

<header>
  <div class="abs header-bg"></div>
  <div class="abs brand-dot"></div>
  <div class="abs brand">HARLOWE</div>
  <div class="abs header-photo" role="img" aria-label="Photo of a woman with a kitten and a bulldog"></div>
  <svg class="abs call-icon" width="14" height="14" viewBox="0 0 14 14"><circle cx="7" cy="7" r="6.2" fill="none" stroke="#555" stroke-width="1"/><path d="M4.6 4c.4-.4.9-.4 1.1 0l.6 1.1c.2.4 0 .7-.3.9l-.3.2c.3.9 1 1.6 1.9 1.9l.2-.3c.2-.3.5-.5.9-.3l1.1.6c.4.2.4.7 0 1.1-.6.6-1.5.8-2.4.3C6 8.7 5.1 7.8 4.4 6.6 3.9 5.6 4 4.7 4.6 4z" fill="#555"/></svg>
  <div class="abs call">Call us Now</div>
  <div class="abs phone">(555) 410-2286</div>
  <div class="abs follow">Follow us on:</div>
  <div class="abs social s1" aria-label="Social profile"></div>
  <div class="abs social s2" aria-label="Social profile"></div>
  <div class="abs social s3" aria-label="Social profile"></div>
</header>

<nav class="abs nav">
  <a class="active" style="left:75px;width:59px">Our Practice</a>
  <a style="left:139px;width:60px">Services</a><span class="sep" style="left:203px"></span>
  <a style="left:208px;width:60px">Our Staff</a><span class="sep" style="left:273px"></span>
  <a style="left:278px;width:72px">Care Guides</a><span class="sep" style="left:356px"></span>
  <a style="left:361px;width:70px">Contact Us</a><span class="sep" style="left:437px"></span>
  <a style="left:442px;width:62px">More Info</a>
  <div class="abs search">Search here
    <svg style="position:absolute;right:4px;top:1px" width="10" height="10" viewBox="0 0 10 10"><circle cx="4" cy="4" r="3" fill="none" stroke="#fff" stroke-width="1.3"/><path d="M6.2 6.2L9 9" stroke="#fff" stroke-width="1.6"/></svg>
  </div>
</nav>

<section>
  <div class="abs hero" role="img" aria-label="Photo of pet owners with a kitten, a puppy and a dog at the vet"></div>
  <svg class="abs hero-curve" width="696" height="90" viewBox="0 0 696 90">
    <defs><linearGradient id="arc" x1="0" x2="1"><stop offset="0" stop-color="#1f5c9c"/><stop offset=".5" stop-color="#2e9c86"/><stop offset="1" stop-color="#2e9c86"/></linearGradient></defs>
    <path d="M0 78 Q348 -38 696 78 L696 90 L0 90 Z" fill="#fff"/>
    <path d="M0 78 Q348 -38 696 78" fill="none" stroke="url(#arc)" stroke-width="4"/>
  </svg>
  <div class="abs dots"><span class="dot off"></span><span class="dot"></span><span class="dot"></span><span class="dot"></span></div>
  <h1 class="abs tagline">Clinic performs medicine, surgery, &amp; wellness care for</h1>
  <div class="abs tag-line" style="left:243px"></div>
  <h2 class="abs tag-big">CAT &amp; DOGS</h2>
  <div class="abs tag-line" style="left:403px"></div>
</section>

<main>
  <div class="abs panel"></div>
  <div class="abs services-panel"></div>

  <div class="abs welcome"></div>
  <div class="abs doc-photo" role="img" aria-label="Photo of the veterinarian holding a spaniel"></div>
  <p class="abs bio">Dr. Owen Marsh received his BS (with distinction) from Eastvale Tech and his DVM from Northbrook University. He and Clara met in veterinary school and married after their sophomore year. He practiced just north of</p>
  <span class="abs read bio-read">Read More...</span>
  <div class="abs badge">Welcome<br>New Clients</div>
  <div class="abs field" style="top:374px">First Name</div>
  <div class="abs field" style="top:390px">Last Name</div>
  <div class="abs field" style="top:407px">Email</div>
  <div class="abs field" style="top:424px">Password</div>
  <div class="abs signup">SIGNUP</div>
  <div class="abs dog-art" role="img" aria-label="Photo of a French bulldog"></div>

  <div class="abs tab" style="left:100px;top:466px;width:172px">Meet A Few Members Of Our Team!</div>
  <div class="abs rope"></div>
  <svg class="abs arrow" style="left:94px" width="18" height="18" viewBox="0 0 18 18"><path d="M1 9 L9 1 L9 6 L17 6 L17 12 L9 12 L9 17 Z" fill="#2e9c86"/></svg>
  <svg class="abs arrow" style="left:581px" width="18" height="18" viewBox="0 0 18 18"><path d="M17 9 L9 1 L9 6 L1 6 L1 12 L9 12 L9 17 Z" fill="#2e9c86"/></svg>

  <div class="abs frame" style="left:120px"><div class="pic" role="img" aria-label="Photo of a staff member with a dog" style="background:linear-gradient(#e3d6bf,#a88d6a 55%,#4e3e2c)"></div><p>Lorem Ipsum is simply dummy text.</p></div>
  <div class="abs frame" style="left:212px"><div class="pic" role="img" aria-label="Photo of clinic staff group" style="background:linear-gradient(#c9bcae,#7a6a60 55%,#3c302c)"></div><p>Lorem Ipsum is simply dummy text.</p></div>
  <div class="abs frame" style="left:304px"><div class="pic" role="img" aria-label="Photo of staff team in purple" style="background:linear-gradient(#b8aeb2,#6e4a68 55%,#3a2238)"></div><p>Lorem Ipsum is simply dummy text.</p></div>
  <div class="abs frame" style="left:398px"><div class="pic" role="img" aria-label="Photo of a staff member seated with pets" style="background:linear-gradient(#d9b08a,#8a5e3c 55%,#4a2e1c)"></div><p>Lorem Ipsum is simply dummy text.</p></div>
  <div class="abs frame" style="left:490px"><div class="pic" role="img" aria-label="Photo of a staff member outdoors with a dog" style="background:linear-gradient(#a7bf96,#5e7a52 55%,#2e3a2a)"></div><p>Lorem Ipsum is simply dummy text.</p></div>
  <div class="abs clip" style="left:158px"></div>
  <div class="abs clip" style="left:250px"></div>
  <div class="abs clip" style="left:342px"></div>
  <div class="abs clip" style="left:436px"></div>
  <div class="abs clip" style="left:528px"></div>

  <div class="abs tab" style="left:100px;top:624px;width:170px">About Harlowe Veterinary Clinic</div>
  <p class="abs about-text">Harlowe Veterinary Clinic is a full-service veterinary medical hospital, located in Brookfield, NC. The professional and courteous staff at Harlowe Veterinary Clinic seeks to provide the best possible medical care, surgical care and dental care for their highly-valued patients. We are committed to promoting responsible pet ownership, preventative health care and health-related educational opportunities for our clients. Ask us about 3 year vaccines and why they are recommended for your pet by veterinary advisory boards internationally.</p>
  <span class="abs read" style="left:294px;top:741px">Read More...</span>
  <div class="abs divider"></div>

  <div class="abs tab" style="left:392px;top:625px;width:104px">Tour Of Clinic</div>
  <div class="abs video" role="img" aria-label="Video still of the clinic building exterior"></div>
  <div class="abs play"></div>
  <svg class="abs" style="left:484px;top:692px" width="8" height="10" viewBox="0 0 8 10"><path d="M0 0L8 5L0 10Z" fill="#fff"/></svg>
  <div class="abs video-bar"></div>

  <div class="abs tab" style="left:100px;top:766px;width:102px">Customer Reviews</div>
  <div class="abs nav-circle" style="left:315px"></div>
  <div class="abs nav-circle" style="left:332px"></div>
  <div class="abs reviewer" role="img" aria-label="Photo of a client with her dog"></div>
  <p class="abs quote"><span class="mark">“</span> Lorem ipsum loremarje roaero joiuroaseoroseroiio Lorem ipsudsfsddloreim loremarje roaero joiuroaseoroseroiiofdLorem ipsum loremarje roaeroLorem ipsudsfsddloreim loremarje roaero joiuroaseoroseroiiofdLorem ipsum loremarje roaero loremireoaoeruouo <span class="mark">”</span></p>

  <div class="abs tab" style="left:392px;top:766px;width:102px">News &amp; Events</div>
  <div class="abs nav-circle" style="left:577px"></div>
  <div class="abs nav-circle" style="left:594px"></div>
  <div class="abs date" style="top:802px"><span class="m">AUG</span><span class="d">12</span></div>
  <p class="abs news-text" style="top:802px">Lorem iarueoiru aesurou loremere loreoaruiouweolraeoae.</p>
  <div class="abs date" style="top:839px"><span class="m">AUG</span><span class="d">12</span></div>
  <p class="abs news-text" style="top:839px">Lorem iarueoiru aesurou loremere loreoaruiouweolraeoae.</p>
  <div class="abs cat-art" role="img" aria-label="Photo of a lying tabby kitten"></div>

  <div class="abs tab" style="left:109px;top:896px;width:74px">Our Services</div>
  <div class="abs svc-dog" role="img" aria-label="Photo of a German shepherd lying down"></div>
  <ul class="abs svc-list" style="left:250px;top:904px">
    <li>Bathing</li><li>Day Care</li><li>Dog Boarding</li><li>Fully Stocked Pharmacy</li>
  </ul>
  <ul class="abs svc-list" style="left:361px;top:904px">
    <li>Internal Medicine</li><li>Microchipping</li><li>Pain Management</li><li>Surgery</li>
  </ul>
  <span class="abs read" style="left:458px;top:947px">View All ...</span>
  <div class="abs svc-cat" role="img" aria-label="Photo of a sitting ginger and white kitten"></div>
</main>

<footer class="footer">
  <svg class="abs footer-wave" width="696" height="146" viewBox="0 0 696 146">
    <defs><linearGradient id="farc" x1="0" x2="1"><stop offset="0" stop-color="#1f5c9c"/><stop offset=".5" stop-color="#2e9c86"/><stop offset="1" stop-color="#2e9c86"/></linearGradient></defs>
    <path d="M0 66 Q348 -36 696 66 L696 146 L0 146 Z" fill="#5b1744"/>
    <path d="M0 62 Q348 -42 696 62" fill="none" stroke="url(#farc)" stroke-width="5"/>
  </svg>

  <h4 style="left:76px;top:1086px">QUICK LINKS</h4>
  <ul class="abs links" style="left:76px;top:1100px">
    <li>• Our Practice</li><li>• Services</li><li>• Our Staff</li><li>• Care Guides</li><li>• Contact Us</li><li>• More Info</li>
  </ul>
  <div class="abs fdiv" style="left:138px"></div>

  <div class="abs cta" style="top:1090px">Schedule an Appointment</div>
  <div class="abs cta" style="top:1115px">Make a Reservation Today</div>
  <div class="abs foot-brand">HARLOWE</div>
  <div class="abs fdiv" style="left:276px"></div>

  <h4 style="left:295px;top:1085px">Clinic Hours</h4>
  <div class="abs hours" style="left:295px;top:1094px">Mon - Weds 7:30 am to &nbsp;7:00 pm<br>Thus Fri 7:00 to 9:00 pm<br>Sat - Sun 9:00 am 5:00 pm</div>
  <div class="abs fdiv" style="left:424px"></div>

  <h4 style="left:444px;top:1085px">Contact Us</h4>
  <div class="abs map" role="img" aria-label="Street map showing the clinic location"></div>
  <div class="abs addr" style="left:526px;top:1100px">2210 Linden Hollow Road<br>Brookfield, NC 27590</div>
  <div class="abs addr" style="left:526px;top:1135px">Phone: (555) 873-0148<br>Fax: (555) 821-0392</div>

  <div class="abs bottom-bar">© 2014, Harlowevc &nbsp;| &nbsp;All Rights Reserved</div>
</footer>

</body>
</html>
```